Zielgruppe
Ich bin Fotograf und habe mich auf Schwangerschafts- und Neugeborenenfotografie spezialisiert. Meine Zielgruppe sind schwangere Frauen im letzten Drittel der Schwangerschaft und frisch gewordene Eltern.
Aufgabenstellung
- sehr schlichtes Design, in der Anlage finden Sie zwei der meist verkauften Karten damit Sie sich vom Stil eine Vorstellung machen können
- Lieferung als offene Indesign 5.5 Datei (so das die Farben, Texte, .... angepasst werden können)
- 2-3 Bilder (querformat) sollen in das Design eingearbeitet werden können
- Die Karten werden von mir nachher als fertig gedruckte Karte an meine Kunden verkauft, dies bitte ich zu berücksichtigen
- ich möchte die Karten so nutzen können das sowohl Geburtskarten für Jungs wie auch für Mädels erstellt werden können
- Format: Din A6 (geschlossen 105x148mm), Klappkarte, hoch, 3mm Beschnitt

```html
<!DOCTYPE html>
<html lang="de">
<head>
<meta charset="utf-8">
<title>Geburtskarte – Präsentation</title>
<link rel="stylesheet" href="https://fonts.googleapis.com/css2?family=Source+Sans+3:wght@400;600&family=Great+Vibes&display=swap">
<style>
  :root {
    --sage: #778a8b;
    --sage-dark: #6a7d7e;
    --pattern-light: #eef2f1;
    --photo-light: #eceeee;
    --photo-mid: #dcdfdf;
    --paper: #ffffff;
    --label: #222222;
    --text-sage: #6f8384;
  }
  * { box-sizing: border-box; margin: 0; padding: 0; }
  html, body { width: 849px; height: 1200px; overflow: hidden; background: var(--paper); }
  body { position: relative; font-family: "Source Sans 3", Arial, sans-serif; }

  .page-label {
    position: absolute;
    transform: translateX(-50%);
    font-size: 11px;
    color: var(--label);
    white-space: nowrap;
  }
  .label-front { left: 277px; top: 95px; transform: translateX(-50%) rotate(-3.7deg); }
  .label-back  { left: 584px; top: 153px; }
  .label-inner { left: 432px; top: 682px; }

  .card-back {
    position: absolute;
    left: 432px; top: 174px;
    width: 304px; height: 429px;
    background: var(--sage);
    box-shadow: 0 1px 2px rgba(0,0,0,.25);
  }
  .card-back .heart { position: absolute; left: 144px; top: 381px; transform: translateY(-50%); }
  .card-back .heart { left: 144px; top: 207px; transform: none; }
  .back-url {
    position: absolute; left: 0; right: 0; bottom: 10px;
    text-align: center; font-size: 7.5px; letter-spacing: .1px;
    color: #fff;
  }

  .card-front {
    position: absolute;
    left: 141px; top: 117px;
    width: 304px; height: 429px;
    background: var(--paper);
    transform: rotate(-3.7deg);
    box-shadow: 0 1px 3px rgba(0,0,0,.25);
    overflow: hidden;
  }
  .front-pattern {
    position: absolute; left: 0; top: 0; width: 100%; height: 213px;
    background: var(--pattern-light);
  }
  .front-photo {
    position: absolute; left: 0; top: 213px; width: 100%; height: 216px;
    background: radial-gradient(ellipse at 60% 60%, #efd9cc 0%, var(--photo-light) 45%, var(--photo-mid) 100%);
  }
  .front-banner {
    position: absolute; left: 106px; top: 200px;
    width: 118px; height: 26px;
    background: var(--sage);
    color: #fff;
    font-size: 15px; letter-spacing: .5px;
    display: flex; align-items: center; justify-content: center;
  }

  .card-inner {
    position: absolute;
    left: 128px; top: 704px;
    width: 608px; height: 428px;
    display: flex;
    box-shadow: 0 1px 2px rgba(0,0,0,.25);
  }
  .inner-left {
    width: 304px; height: 100%;
    background: var(--sage);
    background-image: linear-gradient(var(--sage), var(--sage-dark));
  }
  .inner-right { position: relative; width: 304px; height: 100%; background: var(--paper); }
  .birth-info { position: absolute; left: 0; right: 0; top: 66px; text-align: center; color: var(--text-sage); }
  .baby-name { font-family: "Great Vibes", cursive; font-size: 34px; line-height: 40px; }
  .birth-details { margin-top: 8px; font-size: 9.5px; line-height: 13.5px; }
  .birth-info .heart { margin-top: 10px; }
  .inner-photo {
    position: absolute; left: 0; top: 214px; width: 100%; height: 214px;
    background: radial-gradient(ellipse at 48% 55%, #ecd0c0 0%, #e6e6e6 45%, var(--photo-mid) 100%);
  }
</style>
</head>
<body>
  <div class="page-label label-front">Titelseite</div>
  <div class="page-label label-back">Rückseite</div>
  <div class="page-label label-inner">Innenseiten</div>

  <section class="card-back">
    <svg class="heart" width="16" height="15" viewBox="0 0 24 22" aria-hidden="true">
      <path fill="#fff" d="M12 21.5 2.3 11.8A6 6 0 0 1 12 4.3a6 6 0 0 1 9.7 7.5Z"/>
    </svg>
    <p class="back-url">WWW.KINDERFOTO-LINDENAU.DE</p>
  </section>

  <section class="card-front">
    <div class="front-pattern" role="img" aria-label="Muster aus kleinen hellgrünen Herzen"></div>
    <div class="front-photo" role="img" aria-label="Foto eines schlafenden Neugeborenen auf weißer Decke"></div>
    <div class="front-banner">IT’S A BOY!</div>
  </section>

  <section class="card-inner">
    <div class="inner-left" role="img" aria-label="Muster aus dunkleren Herzen auf graugrünem Grund"></div>
    <div class="inner-right">
      <div class="birth-info">
        <h1 class="baby-name">Linus</h1>
        <p class="birth-details">wurde am 20.03.2012, um 06.45 Uhr geboren,<br>ist 45 cm groß und wiegt 2970 g.</p>
        <svg class="heart" width="16" height="15" viewBox="0 0 24 22" aria-hidden="true">
          <path fill="var(--sage)" d="M12 21.5 2.3 11.8A6 6 0 0 1 12 4.3a6 6 0 0 1 9.7 7.5Z"/>
        </svg>
      </div>
      <div class="inner-photo" role="img" aria-label="Foto eines schlafenden Neugeborenen mit erhobenen Armen"></div>
    </div>
  </section>
</body>
</html>
```